New Business Card Design for Manufacturing

We are an engineering/manufacturing company that offers Advanced machining/assembly/engineering services, as well as innovative products for the heavy duty engine cooling markets.

We are looking to get a new business card designed that is clean and modern looking, but still fits the wide range of technical/skilled work we do.

- We hope to use this design as the base for other design work in new Presentations, web, and print work.

Industry/Entity Type

Engineering

Contact Information for Business Card

Our preferred color of blue is (RGB) 22/71/159 but can vary slightly from that color. Our content will be our Logo and full company name (Fabricated Tooling Works, Inc.), company address, name, job title, phone number with extension, cell number, fax number, website, and email address on the cards.
We'd like the full company name next to the logo, but we are open to other interpretations of that layout.
Preferably, we would like the back side to be clean with just our logo, and the front to contain all of the contact information.

Colors
2f74b4
0355a3
85abd2

Requirements
Must have
• - Logo, company name, needed content - We are open to interpretation beyond that.
• - Standard size business card.
• - Horizontal orientation.
• - Enough space for lengthy names / job titles (for example, a job title could read "Directory of Human Resources" or "V.P. of Governmental Affairs"). We need this to look clean, whether the title be short (CEO) or long (as described above).

```html
<!DOCTYPE html>
<html lang="en">
<head>
<meta charset="utf-8">
<title>Fabricated Tooling Works, Inc. – Business Card</title>
<link rel="stylesheet" href="https://fonts.googleapis.com/css2?family=Roboto:wght@400;500&family=Roboto+Condensed:wght@500;700&display=swap">
<style>
  :root {
    --brand-blue: #0f52a2;
    --card-white: #f1f1f1;
    --ink: #4a4a4a;
    --backdrop: #2b2b2b;
    --white: #ffffff;
  }
  * { margin: 0; padding: 0; box-sizing: border-box; }
  html, body {
    width: 1200px; height: 960px; overflow: hidden;
    background: var(--backdrop);
  }
  .stage { position: relative; width: 1200px; height: 960px; }

  .card {
    position: absolute;
    width: 600px; height: 343px;
    box-shadow: 0 3px 8px rgba(0,0,0,.45);
  }
  .card--front { left: 314px; top: 113px; background: var(--card-white); }
  .card--back  { left: 311px; top: 472px; background: var(--brand-blue); }

  .address {
    position: absolute; left: 46px; top: 47px;
    font-family: "Roboto", sans-serif; font-size: 14px; line-height: 18px;
    color: var(--ink);
  }

  .name-band { position: absolute; left: 0; top: 126px; width: 330px; height: 70px; }
  .identity {
    position: absolute; left: 46px; top: 140px; color: var(--white);
  }
  .identity__name {
    font-family: "Roboto Condensed", sans-serif; font-weight: 500;
    font-size: 22px; line-height: 24px; letter-spacing: .2px;
  }
  .identity__title {
    font-family: "Roboto", sans-serif; font-size: 14px; line-height: 18px;
  }

  .company-name {
    position: absolute; left: 330px; top: 134px; width: 240px;
    font-family: "Roboto Condensed", sans-serif; font-weight: 700;
    font-size: 27px; line-height: 29px; color: var(--brand-blue);
    text-transform: uppercase;
  }

  .contact-list {
    position: absolute; left: 46px; top: 231px; list-style: none;
    font-family: "Roboto", sans-serif; font-size: 14px; line-height: 19px;
    color: var(--ink);
  }
  .contact-list li { display: flex; align-items: center; gap: 8px; }
  .contact-list svg { width: 14px; height: 14px; fill: var(--brand-blue); flex: none; }

  .back-name {
    position: absolute; left: 0; right: 0; top: 140px;
    text-align: center;
    font-family: "Roboto Condensed", sans-serif; font-weight: 700;
    font-size: 34px; line-height: 38px; color: var(--white);
    text-transform: uppercase;
  }
</style>
</head>
<body>
<main class="stage">

  <section class="card card--front" aria-label="Card front">
    <p class="address">2140 Cedar Ridge Road<br>Fairbanks, Alaska 99701</p>

    <svg class="name-band" viewBox="0 0 330 70" aria-hidden="true">
      <polygon points="0,0 330,0 316,70 0,70" fill="var(--brand-blue)"/>
    </svg>
    <div class="identity">
      <p class="identity__name">DANIEL MOREAU</p>
      <p class="identity__title">V.P. of Governmental Affairs</p>
    </div>

    <p class="company-name">Fabricated Tooling Works</p>

    <ul class="contact-list">
      <li>
        <svg viewBox="0 0 24 24" aria-hidden="true"><path d="M6.6 10.8a15 15 0 0 0 6.6 6.6l2.2-2.2c.3-.3.7-.4 1-.2 1.1.4 2.3.6 3.6.6.6 0 1 .4 1 1V20c0 .6-.4 1-1 1A17 17 0 0 1 3 4c0-.6.4-1 1-1h3.5c.6 0 1 .4 1 1 0 1.3.2 2.5.6 3.6.1.3 0 .7-.2 1z"/></svg>
        555 214 8830
      </li>
      <li>
        <svg viewBox="0 0 24 24" aria-hidden="true"><path d="M7 1h10a2 2 0 0 1 2 2v18a2 2 0 0 1-2 2H7a2 2 0 0 1-2-2V3a2 2 0 0 1 2-2zm0 3v14h10V4zm5 15.5a1.2 1.2 0 1 0 0 2.4 1.2 1.2 0 0 0 0-2.4z"/></svg>
        555 317 4472
      </li>
      <li>
        <svg viewBox="0 0 24 24" aria-hidden="true"><path d="M2 6h20v12H2zm2 1.5V8l8 5 8-5v-.5z"/></svg>
        daniel@ftworks.com
      </li>
      <li>
        <svg viewBox="0 0 24 24" aria-hidden="true"><circle cx="12" cy="12" r="10"/></svg>
        www.ftworks.com
      </li>
    </ul>
  </section>

  <section class="card card--back" aria-label="Card back">
    <p class="back-name">Fabricated Tooling Works, Inc.</p>
  </section>

</main>
</body>
</html>
```